Sustainable, ethical bath and beauty care product business needs a Shopify website design.

E-commerce site for environmentally friendly bath and beauty care products company. Our mantra is 'Relax, Re-energize, Reinvent' and and we would like the site to reflect those concepts. We'd like a clean and classy website with rustic and natural nuances. We are also hoping to creatively connect our products to the 5 senses in some way. Looking for retail and wholesale accounts options.

Target Market(s)

Beauty Industry

Industry/Entity Type

Beauty

Coding

Coded - Design and coding required

Colors
EE7325
F08F49
F5BC92
FAE3D3
FDF4ED
6B429C
8869AF
B7A5CE
E3DAEB
F3F0F8

Requirements
Must have
• Sliding Banner included is the of the tree we submitted.

```html
<!DOCTYPE html>
<html lang="en">
<head>
<meta charset="utf-8">
<title>Aurelle Goods – Home Page Design</title>
<link href="https://fonts.googleapis.com/css2?family=Lora:ital,wght@0,400;0,600;0,700;1,400&display=swap" rel="stylesheet">
<style>
:root{
  --orange:#EE7325;
  --orange-2:#F08F49;
  --orange-3:#F5BC92;
  --orange-4:#FAE3D3;
  --purple:#6B429C;
  --purple-deep:#512C76;
  --purple-2:#8869AF;
  --purple-3:#B7A5CE;
  --lilac:#E3DAEB;
  --board:#F3F4F6;
  --section-grey:#F4F5F7;
  --ink:#3a3a3a;
  --muted:#6d6d6d;
  --line:#e2e2e2;
  --white:#ffffff;
}
*{box-sizing:border-box;margin:0;padding:0}
html,body{width:767px;height:1200px;overflow:hidden}
body{background:var(--board);font-family:"Lora",Georgia,serif;color:var(--ink);position:relative}
.page{position:absolute;top:26.4px;width:719px;height:2285px;background:var(--white);transform:scale(.4984);transform-origin:0 0;box-shadow:0 2px 10px rgba(0,0,0,.12);overflow:hidden}
.page--default{left:19.5px}
.page--menu-open{left:391.3px}

/* header */
.site-header{position:absolute;left:0;top:0;width:719px;height:80px;background:var(--white);border-bottom:1px solid #eee}
.brand{position:absolute;left:66px;top:32px;display:flex;align-items:center;gap:6px;white-space:nowrap}
.brand-dot{width:12px;height:12px;border-radius:50%;background:var(--orange);flex:none}
.brand-name{font-size:13px;font-weight:600;color:var(--purple);letter-spacing:1.5px;text-transform:uppercase}
.main-nav{position:absolute;top:36px;left:0;font-size:9px;color:var(--ink);letter-spacing:.3px}
.main-nav span{position:absolute;white-space:nowrap}
.header-tools{position:absolute;left:578px;top:35px;display:flex;gap:9px}
.header-tools svg{width:11px;height:11px;fill:var(--orange)}

/* hero */
.hero{position:absolute;top:80px;left:0;width:719px;height:386px;background:linear-gradient(90deg,#d9e9e2 0%,#e4efec 35%,#e2eeee 100%)}
.hero-photo{position:absolute;inset:0;background:radial-gradient(ellipse 170px 230px at 150px 170px,rgba(120,180,90,.35),rgba(255,255,255,0) 70%),radial-gradient(ellipse 90px 60px at 250px 320px,rgba(255,250,235,.7),rgba(255,255,255,0) 80%)}
.hero-title{position:absolute;left:340px;top:203px;width:330px;text-align:center;font-size:25px;font-weight:400;color:var(--purple);letter-spacing:.3px}
.hero-sub{position:absolute;left:354px;top:237px;width:302px;display:flex;align-items:center;gap:6px;font-size:25px;color:var(--orange);white-space:nowrap}
.hero-sub::before,.hero-sub::after{content:"";flex:1;height:1.5px;background:var(--orange)}

/* promo band */
.promo{position:absolute;top:466px;left:0;width:719px;height:253px;background:var(--orange)}
.promo-heading{position:absolute;left:67px;top:76px;color:var(--white);font-size:15px;font-weight:600;line-height:27px;letter-spacing:0;white-space:nowrap}
.promo-copy{position:absolute;left:67px;top:138px;width:262px;color:var(--white);font:7.5px/15.5px Arial,Helvetica,sans-serif}
.promo-photo{position:absolute;left:350px;top:24px;width:369px;height:229px;border-radius:90px 0 0 40px;background:linear-gradient(120deg,#7a4a2a 0%,#f7f2e6 28%,#f3e6b8 55%,#efe9d6 75%,#3d5a25 100%);opacity:.92}

/* values */
.values{position:absolute;top:719px;left:0;width:719px;height:204px;background:var(--white)}
.value{position:absolute;top:30px;width:160px;text-align:center}
.value-icon{width:90px;height:90px;margin:0 auto;border-radius:50%;display:flex;align-items:center;justify-content:center;box-shadow:0 0 0 2px var(--white),0 0 0 3.5px currentColor}
.value-icon svg{width:40px;height:40px;fill:none;stroke:var(--white);stroke-width:2;stroke-linecap:round;stroke-linejoin:round}
.value--purple{color:var(--purple-deep)}
.value--purple .value-icon{background:var(--purple-deep)}
.value--orange{color:var(--orange)}
.value--orange .value-icon{background:var(--orange)}
.value-title{margin-top:12px;font-size:13px;font-weight:700}
.value-note{font-size:9.5px;font-style:italic;color:var(--muted)}

/* products */
.products{position:absolute;left:0;width:719px;height:320px;background:var(--section-grey)}
.section-title{position:absolute;left:0;width:719px;text-align:center;font-size:17px;font-weight:600;color:var(--ink);letter-spacing:.3px}
.section-title::after{content:"";display:block;width:30px;height:2px;background:var(--orange);margin:8px auto 0}
.card{position:absolute;top:78px;width:141px;height:192px;background:var(--white);border:1px solid var(--line);box-shadow:0 1px 3px rgba(0,0,0,.06);text-align:center}
.fav{position:absolute;left:7px;top:11px;width:20px;height:20px;border-radius:50%;background:#cfcfcf;display:flex;align-items:center;justify-content:center;z-index:1}
.fav svg{width:10px;height:10px;fill:none;stroke:var(--white);stroke-width:2.4}
.fav--active{background:var(--orange)}
.shot{position:absolute;left:12px;top:24px;width:116px;height:92px;border-radius:6px}
.card-name{position:absolute;left:0;right:0;top:132px;font-size:13px;color:var(--ink)}
.card-price{position:absolute;left:0;right:0;top:155px;font-size:13px;font-weight:700;color:var(--orange)}
.card-cta{position:absolute;left:0;right:0;top:156px;font-size:11.5px;color:var(--orange);text-decoration:underline}

/* senses */
.senses{position:absolute;top:1242px;left:0;width:719px;height:233px;background:linear-gradient(110deg,#5a2f78 0%,#8a4a5a 40%,#c25b32 70%,#ee6e1e 100%)}
.sense{position:absolute;width:111px;height:110px;border:1.5px solid rgba(255,255,255,.9);color:var(--white);text-align:center}
.sense svg{position:absolute;left:35px;top:15px;width:40px;height:40px;fill:none;stroke:var(--white);stroke-width:2;stroke-linecap:round;stroke-linejoin:round}
.sense span{position:absolute;left:0;right:0;top:72px;font-size:12px;font-weight:700}

/* testimonial */
.testimonial{position:absolute;top:1795px;left:0;width:719px;height:259px;background:var(--white)}
.client-photo{position:absolute;left:93px;top:53px;width:155px;height:155px;border-radius:50%;background:radial-gradient(circle at 50% 40%,#f3ede8 0%,#e2dcd6 55%,#b9b4b0 100%)}
.quote-badge{position:absolute;left:153px;top:192px;width:34px;height:34px;border-radius:50%;background:var(--orange);color:var(--white);font-size:22px;font-weight:700;text-align:center;line-height:40px}
.testimonial-title{position:absolute;left:278px;top:50px;font-size:24px;font-weight:700;color:var(--ink)}
.testimonial-copy{position:absolute;left:280px;top:98px;width:346px;font:italic 8px/16px Arial,Helvetica,sans-serif;color:var(--muted);text-align:justify}
.testimonial-sign{position:absolute;left:278px;top:190px;font-size:12px;font-weight:700;color:var(--orange)}
.testimonial-sign small{font:400 8px Arial,Helvetica,sans-serif;color:var(--ink)}

/* footer */
.site-footer{position:absolute;top:2054px;left:0;width:719px;height:231px;background:var(--purple-deep);color:var(--white)}
.footer-brand{position:absolute;left:0;width:719px;top:60px;display:flex;justify-content:center;align-items:center;gap:8px}
.footer-brand .brand-name{color:var(--white);font-size:20px;letter-spacing:2px}
.footer-brand .brand-dot{background:var(--white);width:14px;height:14px}
.contact{position:absolute;top:116px;display:flex;align-items:center;gap:14px;font-size:12.5px;line-height:16px;white-space:nowrap}
.contact-icon{width:42px;height:42px;border-radius:50%;border:2px solid rgba(255,255,255,.35);display:flex;align-items:center;justify-content:center}
.contact-icon svg{width:13px;height:13px;fill:var(--white)}
.social{position:absolute;left:67px;top:198px;display:flex;gap:4px}
.social span{width:21px;height:21px;border-radius:50%;border:1.5px solid var(--white)}
.copyright{position:absolute;right:68px;top:202px;font-size:9.5px;white-space:nowrap}
.copyright u{margin-left:2px}
.page-code{position:absolute;right:47px;top:220px;font-size:8px}

/* mega menu */
.mega-menu{position:absolute;left:265px;top:68px;width:430px;height:148px;background:var(--white);border:2px solid var(--purple-deep)}
.mega-menu::before{content:"";position:absolute;left:13px;top:-8px;border:6px solid transparent;border-bottom-color:var(--purple-deep);border-top:0}
.menu-col{position:absolute;font-size:8px;color:var(--ink)}
.menu-col h4{font-size:11px;font-weight:700;color:var(--purple-deep);margin-bottom:8px}
.menu-col li{list-style:none;margin-bottom:6px;white-space:nowrap}
.menu-col li::before{content:"»";margin-right:5px}
</style>
</head>
<body>

<!-- default state -->
<section class="page page--default">
  <header class="site-header">
    <div class="brand"><span class="brand-dot"></span><span class="brand-name">Aurelle Goods</span></div>
    <nav class="main-nav">
      <span style="left:267px">BATH</span><span style="left:318px">BODY</span><span style="left:370px">FACE</span><span style="left:419px">CANDLES</span><span style="left:487px">KIDS</span><span style="left:535px">PETS</span>
    </nav>
    <div class="header-tools">
      <svg viewBox="0 0 24 24"><path d="M10 3a7 7 0 0 1 5.6 11.2l5.1 5.1-1.6 1.6-5.1-5.1A7 7 0 1 1 10 3zm0 3a4 4 0 1 0 0 8 4 4 0 0 0 0-8z"/></svg>
      <svg viewBox="0 0 24 24"><circle cx="12" cy="7" r="5"/><path d="M3 22c0-5 4-8 9-8s9 3 9 8z"/></svg>
      <svg viewBox="0 0 24 24"><path d="M12 21l-1.5-1.3C5 15 2 12 2 8.5 2 5.5 4.4 3 7.5 3c1.7 0 3.4.8 4.5 2.1C13.1 3.8 14.8 3 16.5 3 19.6 3 22 5.5 22 8.5c0 3.5-3 6.5-8.5 11.2z"/></svg>
      <svg viewBox="0 0 24 24"><path d="M2 3h3l3 12h11l3-9H7l-.6-3zM9 18a2 2 0 1 1 0 4 2 2 0 0 1 0-4zm9 0a2 2 0 1 1 0 4 2 2 0 0 1 0-4z"/></svg>
    </div>
  </header>

  <section class="hero">
    <div class="hero-photo" role="img" aria-label="Banner photo of white skincare bottles, a cream jar and green fern leaves"></div>
    <h1 class="hero-title">ALL ABOUT SUSTAINABLE</h1>
    <p class="hero-sub">BEAUTY PRODUCTS</p>
  </section>

  <section class="promo">
    <h2 class="promo-heading">SED UT PERSPICIATIS<br>UNDE OMNIS ISTE NATUS ERROR</h2>
    <p class="promo-copy">Nemo enim ipsam voluptatem quia voluptas sit aspernatur aut odit aut fugit, sed quia consequuntur magni dolores eos qui ratione voluptatem voluptatem quia voluptas sit aspernatur sequi nesciunt.</p>
    <div class="promo-photo" role="img" aria-label="Photo of handmade soap bars tied with twine beside a split coconut and olive leaves"></div>
  </section>

  <section class="values">
    <div class="value value--purple" style="left:81px">
      <div class="value-icon"><svg viewBox="0 0 40 40"><path d="M15 10l5-7 5 7M11 30H4l4-8M29 30h7l-4-8M17 30h6M14 16l-4 6M26 16l4 6"/></svg></div>
      <p class="value-title">REINVENT</p><p class="value-note">Sustainability</p>
    </div>
    <div class="value value--orange" style="left:281px">
      <div class="value-icon"><svg viewBox="0 0 40 40"><path d="M6 26c6 4 22 4 28-4M10 22c4-8 14-12 22-8M14 18l6 6M22 12a3 3 0 1 0 6 0 3 3 0 0 0-6 0"/></svg></div>
      <p class="value-title">RELAX</p><p class="value-note">Masterfully Crafted</p>
    </div>
    <div class="value value--purple" style="left:481px">
      <div class="value-icon"><svg viewBox="0 0 40 40"><path d="M20 6c-6 6-6 14 0 20 6-6 6-14 0-20zM20 10v22M6 18c0 8 6 14 12 16M34 18c0 8-6 14-12 16"/></svg></div>
      <p class="value-title">RE-ENERGIZE</p><p class="value-note">All Natural</p>
    </div>
  </section>

  <section class="products" style="top:923px">
    <h2 class="section-title" style="top:27px">FEATURED PRODUCTS</h2>
    <div class="card" style="left:67px"><span class="fav"><svg viewBox="0 0 24 24"><path d="M12 20l-1.2-1C5.5 14.5 3 12 3 8.8 3 6.2 5 4 7.6 4c1.6 0 3.2.8 4.4 2 1.2-1.2 2.8-2 4.4-2C19 4 21 6.2 21 8.8c0 3.2-2.5 5.7-7.8 10.2z"/></svg></span><div class="shot" role="img" aria-label="Product photo of cosmetic jars and a gold lip gloss" style="background:linear-gradient(180deg,#fff 10%,#efe6dc 60%,#d4c1a8 100%)"></div><p class="card-name">Product Name</p><p class="card-price">$25.00</p></div>
    <div class="card" style="left:215px"><span class="fav fav--active"><svg viewBox="0 0 24 24"><path d="M12 20l-1.2-1C5.5 14.5 3 12 3 8.8 3 6.2 5 4 7.6 4c1.6 0 3.2.8 4.4 2 1.2-1.2 2.8-2 4.4-2C19 4 21 6.2 21 8.8c0 3.2-2.5 5.7-7.8 10.2z"/></svg></span><div class="shot" role="img" aria-label="Product photo of bath salts with lavender and a purple towel" style="background:linear-gradient(100deg,#b69ac8 0%,#f1c78e 45%,#7b5bb0 100%)"></div><p class="card-name">Product Name</p><p class="card-cta">Add to cart</p></div>
    <div class="card" style="left:363px"><span class="fav"><svg viewBox="0 0 24 24"><path d="M12 20l-1.2-1C5.5 14.5 3 12 3 8.8 3 6.2 5 4 7.6 4c1.6 0 3.2.8 4.4 2 1.2-1.2 2.8-2 4.4-2C19 4 21 6.2 21 8.8c0 3.2-2.5 5.7-7.8 10.2z"/></svg></span><div class="shot" role="img" aria-label="Product photo of a yellow lip balm stick" style="background:radial-gradient(ellipse at 55% 55%,#f2b21c 0%,#f7d67c 35%,#fff 75%)"></div><p class="card-name">Product Name</p><p class="card-price">$25.00</p></div>
    <div class="card" style="left:511px"><span class="fav"><svg viewBox="0 0 24 24"><path d="M12 20l-1.2-1C5.5 14.5 3 12 3 8.8 3 6.2 5 4 7.6 4c1.6 0 3.2.8 4.4 2 1.2-1.2 2.8-2 4.4-2C19 4 21 6.2 21 8.8c0 3.2-2.5 5.7-7.8 10.2z"/></svg></span><div class="shot" role="img" aria-label="Product photo of a herbal soap bar tied with twine" style="background:radial-gradient(ellipse at 50% 55%,#9a8a55 0%,#c8b27e 40%,#fff 78%)"></div><p class="card-name">Product Name</p><p class="card-price">$25.00</p></div>
  </section>

  <section class="senses">
    <div class="sense" style="left:67px;top:37px"><svg viewBox="0 0 40 40"><path d="M16 20V8a3 3 0 0 1 6 0v10l8 2c3 1 4 3 3 6l-2 8H17l-6-9c-1-2 1-4 3-3l2 2M12 10a8 8 0 0 1 14 0"/></svg><span>TOUCH</span></div>
    <div class="sense" style="left:186px;top:85px"><svg viewBox="0 0 40 40"><path d="M24 4c-2 8-10 14-10 20 0 3 3 4 6 3M10 28c-2 2-3 5-3 8M15 31c-2 1-3 3-3 6M20 33c-1 1-2 2-2 4"/></svg><span>SMELL</span></div>
    <div class="sense" style="left:304px;top:37px"><svg viewBox="0 0 40 40"><path d="M2 20s7-11 18-11 18 11 18 11-7 11-18 11S2 20 2 20z"/><circle cx="20" cy="20" r="7"/><circle cx="20" cy="20" r="3"/></svg><span>VISION</span></div>
    <div class="sense" style="left:422px;top:85px"><svg viewBox="0 0 40 40"><circle cx="20" cy="20" r="17"/><path d="M12 16q2-2 4 0M24 16q2-2 4 0M13 25q7 6 14 0M20 27q0 5 4 5"/></svg><span>TASTE</span></div>
    <div class="sense" style="left:541px;top:37px"><svg viewBox="0 0 40 40"><path d="M18 32c4 2 8-1 8-5 0-5 8-7 8-15A10 10 0 0 0 14 12M20 13a4 4 0 0 1 8 0c0 3-4 4-4 7M2 20h4l2-5 3 10 2-5h3"/></svg><span>HEARING</span></div>
  </section>

  <section class="products" style="top:1475px">
    <h2 class="section-title" style="top:27px">TOP SELLERS</h2>
    <div class="card" style="left:67px"><span class="fav"><svg viewBox="0 0 24 24"><path d="M12 20l-1.2-1C5.5 14.5 3 12 3 8.8 3 6.2 5 4 7.6 4c1.6 0 3.2.8 4.4 2 1.2-1.2 2.8-2 4.4-2C19 4 21 6.2 21 8.8c0 3.2-2.5 5.7-7.8 10.2z"/></svg></span><div class="shot" role="img" aria-label="Product photo of shea butter with shea nuts on a wooden dish" style="background:radial-gradient(ellipse at 55% 50%,#f3ead8 0%,#d9b98f 40%,#6e4e35 60%,#fff 80%)"></div><p class="card-name">Product Name</p><p class="card-price">$25.00</p></div>
    <div class="card" style="left:215px"><span class="fav fav--active"><svg viewBox="0 0 24 24"><path d="M12 20l-1.2-1C5.5 14.5 3 12 3 8.8 3 6.2 5 4 7.6 4c1.6 0 3.2.8 4.4 2 1.2-1.2 2.8-2 4.4-2C19 4 21 6.2 21 8.8c0 3.2-2.5 5.7-7.8 10.2z"/></svg></span><div class="shot" role="img" aria-label="Product photo of purple bath salt spilling from a wooden bowl" style="background:radial-gradient(ellipse at 50% 60%,#7b3fc4 0%,#9a6ad1 40%,#a4683d 55%,#fff 80%)"></div><p class="card-name">Product Name</p><p class="card-cta">Add to cart</p></div>
    <div class="card" style="left:363px"><span class="fav"><svg viewBox="0 0 24 24"><path d="M12 20l-1.2-1C5.5 14.5 3 12 3 8.8 3 6.2 5 4 7.6 4c1.6 0 3.2.8 4.4 2 1.2-1.2 2.8-2 4.4-2C19 4 21 6.2 21 8.8c0 3.2-2.5 5.7-7.8 10.2z"/></svg></span><div class="shot" role="img" aria-label="Product photo of an open pink lip scrub jar with a green lid" style="background:linear-gradient(100deg,#fff 0%,#f0307a 30%,#f56aa6 50%,#86d42b 75%,#fff 100%)"></div><p class="card-name">Product Name</p><p class="card-price">$25.00</p></div>
    <div class="card" style="left:511px"><span class="fav"><svg viewBox="0 0 24 24"><path d="M12 20l-1.2-1C5.5 14.5 3 12 3 8.8 3 6.2 5 4 7.6 4c1.6 0 3.2.8 4.4 2 1.2-1.2 2.8-2 4.4-2C19 4 21 6.2 21 8.8c0 3.2-2.5 5.7-7.8 10.2z"/></svg></span><div class="shot" role="img" aria-label="Product photo of layered orange pillar candles with berries" style="background:linear-gradient(180deg,#fff 0%,#f4a05a 35%,#c8542a 70%,#7a3d22 100%)"></div><p class="card-name">Product Name</p><p class="card-price">$25.00</p></div>
  </section>

  <section class="testimonial">
    <div class="client-photo" role="img" aria-label="Portrait photo of a smiling customer"></div>
    <div class="quote-badge">”</div>
    <h2 class="testimonial-title">TESTIMONIALS</h2>
    <p class="testimonial-copy">Sed ut perspiciatis unde omnis iste natus error sit voluptatem accusantium doloremque laudantium, totam rem aperiam, eaque ipsa quae ab illo inventore veritatis et quasi architecto beatae vitae dicta sunt explicabo. Nemo enim ipsam voluptatem quia voluptas sit aspernatur aut odit aut fugit, sed quia consequuntur magni dolores eos qui ratione labore et dolore magnam omnis iste natus error sit aliquam quaerat voluptatem.</p>
    <p class="testimonial-sign">Mara Ellis,<small>Sed ut perspiciatis unde</small></p>
  </section>

  <footer class="site-footer">
    <div class="footer-brand"><span class="brand-dot"></span><span class="brand-name">Aurelle Goods</span></div>
    <div class="contact" style="left:96px"><span class="contact-icon"><svg viewBox="0 0 24 24"><path d="M6.6 10.8a15 15 0 0 0 6.6 6.6l2.2-2.2c.3-.3.7-.4 1-.2 1.1.4 2.3.6 3.6.6.6 0 1 .4 1 1V20c0 .6-.4 1-1 1A17 17 0 0 1 3 4c0-.6.4-1 1-1h3.5c.6 0 1 .4 1 1 0 1.3.2 2.5.6 3.6.1.3 0 .7-.2 1z"/></svg></span><span>Phone<br>000.121.1231</span></div>
    <div class="contact" style="left:297px"><span class="contact-icon"><svg viewBox="0 0 24 24"><path d="M2 5h20v14H2zm2 2v.5l8 5 8-5V7l-8 5z"/></svg></span><span>Email<br>info@company.com</span></div>
    <div class="contact" style="left:484px"><span class="contact-icon"><svg viewBox="0 0 24 24"><path d="M12 2a7 7 0 0 1 7 7c0 5-7 13-7 13S5 14 5 9a7 7 0 0 1 7-7zm0 4a3 3 0 1 0 0 6 3 3 0 0 0 0-6z"/></svg></span><span>154 Lorem Ipsum<br>Dummy Lorem</span></div>
    <div class="social"><span></span><span></span><span></span><span></span><span></span></div>
    <p class="copyright">© Copyright 2022 Aurelle Goods.All Rights Reserved.<u>Meet The Team</u></p>
    <p class="page-code">C2</p>
  </footer>
</section>

<!-- menu open state -->
<section class="page page--menu-open">
  <header class="site-header">
    <div class="brand"><span class="brand-dot"></span><span class="brand-name">Aurelle Goods</span></div>
    <nav class="main-nav">
      <span style="left:267px">BATH</span><span style="left:318px">BODY</span><span style="left:370px">FACE</span><span style="left:419px">CANDLES</span><span style="left:487px">KIDS</span><span style="left:535px">PETS</span>
    </nav>
    <div class="header-tools">
      <svg viewBox="0 0 24 24"><path d="M10 3a7 7 0 0 1 5.6 11.2l5.1 5.1-1.6 1.6-5.1-5.1A7 7 0 1 1 10 3zm0 3a4 4 0 1 0 0 8 4 4 0 0 0 0-8z"/></svg>
      <svg viewBox="0 0 24 24"><circle cx="12" cy="7" r="5"/><path d="M3 22c0-5 4-8 9-8s9 3 9 8z"/></svg>
      <svg viewBox="0 0 24 24"><path d="M12 21l-1.5-1.3C5 15 2 12 2 8.5 2 5.5 4.4 3 7.5 3c1.7 0 3.4.8 4.5 2.1C13.1 3.8 14.8 3 16.5 3 19.6 3 22 5.5 22 8.5c0 3.5-3 6.5-8.5 11.2z"/></svg>
      <svg viewBox="0 0 24 24"><path d="M2 3h3l3 12h11l3-9H7l-.6-3zM9 18a2 2 0 1 1 0 4 2 2 0 0 1 0-4zm9 0a2 2 0 1 1 0 4 2 2 0 0 1 0-4z"/></svg>
    </div>
  </header>

  <section class="hero">
    <div class="hero-photo" role="img" aria-label="Banner photo of white skincare bottles, a cream jar and green fern leaves"></div>
    <h1 class="hero-title">ALL ABOUT SUSTAINABLE</h1>
    <p class="hero-sub">BEAUTY PRODUCTS</p>
  </section>

  <section class="promo">
    <h2 class="promo-heading">SED UT PERSPICIATIS<br>UNDE OMNIS ISTE NATUS ERROR</h2>
    <p class="promo-copy">Nemo enim ipsam voluptatem quia voluptas sit aspernatur aut odit aut fugit, sed quia consequuntur magni dolores eos qui ratione voluptatem voluptatem quia voluptas sit aspernatur sequi nesciunt.</p>
    <div class="promo-photo" role="img" aria-label="Photo of handmade soap bars tied with twine beside a split coconut and olive leaves"></div>
  </section>

  <section class="values">
    <div class="value value--purple" style="left:81px">
      <div class="value-icon"><svg viewBox="0 0 40 40"><path d="M15 10l5-7 5 7M11 30H4l4-8M29 30h7l-4-8M17 30h6M14 16l-4 6M26 16l4 6"/></svg></div>
      <p class="value-title">REINVENT</p><p class="value-note">Sustainability</p>
    </div>
    <div class="value value--orange" style="left:281px">
      <div class="value-icon"><svg viewBox="0 0 40 40"><path d="M6 26c6 4 22 4 28-4M10 22c4-8 14-12 22-8M14 18l6 6M22 12a3 3 0 1 0 6 0 3 3 0 0 0-6 0"/></svg></div>
      <p class="value-title">RELAX</p><p class="value-note">Masterfully Crafted</p>
    </div>
    <div class="value value--purple" style="left:481px">
      <div class="value-icon"><svg viewBox="0 0 40 40"><path d="M20 6c-6 6-6 14 0 20 6-6 6-14 0-20zM20 10v22M6 18c0 8 6 14 12 16M34 18c0 8-6 14-12 16"/></svg></div>
      <p class="value-title">RE-ENERGIZE</p><p class="value-note">All Natural</p>
    </div>
  </section>

  <section class="products" style="top:923px">
    <h2 class="section-title" style="top:27px">FEATURED PRODUCTS</h2>
    <div class="card" style="left:67px"><span class="fav"><svg viewBox="0 0 24 24"><path d="M12 20l-1.2-1C5.5 14.5 3 12 3 8.8 3 6.2 5 4 7.6 4c1.6 0 3.2.8 4.4 2 1.2-1.2 2.8-2 4.4-2C19 4 21 6.2 21 8.8c0 3.2-2.5 5.7-7.8 10.2z"/></svg></span><div class="shot" role="img" aria-label="Product photo of cosmetic jars and a gold lip gloss" style="background:linear-gradient(180deg,#fff 10%,#efe6dc 60%,#d4c1a8 100%)"></div><p class="card-name">Product Name</p><p class="card-price">$25.00</p></div>
    <div class="card" style="left:215px"><span class="fav fav--active"><svg viewBox="0 0 24 24"><path d="M12 20l-1.2-1C5.5 14.5 3 12 3 8.8 3 6.2 5 4 7.6 4c1.6 0 3.2.8 4.4 2 1.2-1.2 2.8-2 4.4-2C19 4 21 6.2 21 8.8c0 3.2-2.5 5.7-7.8 10.2z"/></svg></span><div class="shot" role="img" aria-label="Product photo of bath salts with lavender and a purple towel" style="background:linear-gradient(100deg,#b69ac8 0%,#f1c78e 45%,#7b5bb0 100%)"></div><p class="card-name">Product Name</p><p class="card-cta">Add to cart</p></div>
    <div class="card" style="left:363px"><span class="fav"><svg viewBox="0 0 24 24"><path d="M12 20l-1.2-1C5.5 14.5 3 12 3 8.8 3 6.2 5 4 7.6 4c1.6 0 3.2.8 4.4 2 1.2-1.2 2.8-2 4.4-2C19 4 21 6.2 21 8.8c0 3.2-2.5 5.7-7.8 10.2z"/></svg></span><div class="shot" role="img" aria-label="Product photo of a yellow lip balm stick" style="background:radial-gradient(ellipse at 55% 55%,#f2b21c 0%,#f7d67c 35%,#fff 75%)"></div><p class="card-name">Product Name</p><p class="card-price">$25.00</p></div>
    <div class="card" style="left:511px"><span class="fav"><svg viewBox="0 0 24 24"><path d="M12 20l-1.2-1C5.5 14.5 3 12 3 8.8 3 6.2 5 4 7.6 4c1.6 0 3.2.8 4.4 2 1.2-1.2 2.8-2 4.4-2C19 4 21 6.2 21 8.8c0 3.2-2.5 5.7-7.8 10.2z"/></svg></span><div class="shot" role="img" aria-label="Product photo of a herbal soap bar tied with twine" style="background:radial-gradient(ellipse at 50% 55%,#9a8a55 0%,#c8b27e 40%,#fff 78%)"></div><p class="card-name">Product Name</p><p class="card-price">$25.00</p></div>
  </section>

  <section class="senses">
    <div class="sense" style="left:67px;top:37px"><svg viewBox="0 0 40 40"><path d="M16 20V8a3 3 0 0 1 6 0v10l8 2c3 1 4 3 3 6l-2 8H17l-6-9c-1-2 1-4 3-3l2 2M12 10a8 8 0 0 1 14 0"/></svg><span>TOUCH</span></div>
    <div class="sense" style="left:186px;top:85px"><svg viewBox="0 0 40 40"><path d="M24 4c-2 8-10 14-10 20 0 3 3 4 6 3M10 28c-2 2-3 5-3 8M15 31c-2 1-3 3-3 6M20 33c-1 1-2 2-2 4"/></svg><span>SMELL</span></div>
    <div class="sense" style="left:304px;top:37px"><svg viewBox="0 0 40 40"><path d="M2 20s7-11 18-11 18 11 18 11-7 11-18 11S2 20 2 20z"/><circle cx="20" cy="20" r="7"/><circle cx="20" cy="20" r="3"/></svg><span>VISION</span></div>
    <div class="sense" style="left:422px;top:85px"><svg viewBox="0 0 40 40"><circle cx="20" cy="20" r="17"/><path d="M12 16q2-2 4 0M24 16q2-2 4 0M13 25q7 6 14 0M20 27q0 5 4 5"/></svg><span>TASTE</span></div>
    <div class="sense" style="left:541px;top:37px"><svg viewBox="0 0 40 40"><path d="M18 32c4 2 8-1 8-5 0-5 8-7 8-15A10 10 0 0 0 14 12M20 13a4 4 0 0 1 8 0c0 3-4 4-4 7M2 20h4l2-5 3 10 2-5h3"/></svg><span>HEARING</span></div>
  </section>

  <section class="products" style="top:1475px">
    <h2 class="section-title" style="top:27px">TOP SELLERS</h2>
    <div class="card" style="left:67px"><span class="fav"><svg viewBox="0 0 24 24"><path d="M12 20l-1.2-1C5.5 14.5 3 12 3 8.8 3 6.2 5 4 7.6 4c1.6 0 3.2.8 4.4 2 1.2-1.2 2.8-2 4.4-2C19 4 21 6.2 21 8.8c0 3.2-2.5 5.7-7.8 10.2z"/></svg></span><div class="shot" role="img" aria-label="Product photo of shea butter with shea nuts on a wooden dish" style="background:radial-gradient(ellipse at 55% 50%,#f3ead8 0%,#d9b98f 40%,#6e4e35 60%,#fff 80%)"></div><p class="card-name">Product Name</p><p class="card-price">$25.00</p></div>
    <div class="card" style="left:215px"><span class="fav fav--active"><svg viewBox="0 0 24 24"><path d="M12 20l-1.2-1C5.5 14.5 3 12 3 8.8 3 6.2 5 4 7.6 4c1.6 0 3.2.8 4.4 2 1.2-1.2 2.8-2 4.4-2C19 4 21 6.2 21 8.8c0 3.2-2.5 5.7-7.8 10.2z"/></svg></span><div class="shot" role="img" aria-label="Product photo of purple bath salt spilling from a wooden bowl" style="background:radial-gradient(ellipse at 50% 60%,#7b3fc4 0%,#9a6ad1 40%,#a4683d 55%,#fff 80%)"></div><p class="card-name">Product Name</p><p class="card-cta">Add to cart</p></div>
    <div class="card" style="left:363px"><span class="fav"><svg viewBox="0 0 24 24"><path d="M12 20l-1.2-1C5.5 14.5 3 12 3 8.8 3 6.2 5 4 7.6 4c1.6 0 3.2.8 4.4 2 1.2-1.2 2.8-2 4.4-2C19 4 21 6.2 21 8.8c0 3.2-2.5 5.7-7.8 10.2z"/></svg></span><div class="shot" role="img" aria-label="Product photo of an open pink lip scrub jar with a green lid" style="background:linear-gradient(100deg,#fff 0%,#f0307a 30%,#f56aa6 50%,#86d42b 75%,#fff 100%)"></div><p class="card-name">Product Name</p><p class="card-price">$25.00</p></div>
    <div class="card" style="left:511px"><span class="fav"><svg viewBox="0 0 24 24"><path d="M12 20l-1.2-1C5.5 14.5 3 12 3 8.8 3 6.2 5 4 7.6 4c1.6 0 3.2.8 4.4 2 1.2-1.2 2.8-2 4.4-2C19 4 21 6.2 21 8.8c0 3.2-2.5 5.7-7.8 10.2z"/></svg></span><div class="shot" role="img" aria-label="Product photo of layered orange pillar candles with berries" style="background:linear-gradient(180deg,#fff 0%,#f4a05a 35%,#c8542a 70%,#7a3d22 100%)"></div><p class="card-name">Product Name</p><p class="card-price">$25.00</p></div>
  </section>

  <section class="testimonial">
    <div class="client-photo" role="img" aria-label="Portrait photo of a smiling customer"></div>
    <div class="quote-badge">”</div>
    <h2 class="testimonial-title">TESTIMONIALS</h2>
    <p class="testimonial-copy">Sed ut perspiciatis unde omnis iste natus error sit voluptatem accusantium doloremque laudantium, totam rem aperiam, eaque ipsa quae ab illo inventore veritatis et quasi architecto beatae vitae dicta sunt explicabo. Nemo enim ipsam voluptatem quia voluptas sit aspernatur aut odit aut fugit, sed quia consequuntur magni dolores eos qui ratione labore et dolore magnam omnis iste natus error sit aliquam quaerat voluptatem.</p>
    <p class="testimonial-sign">Mara Ellis,<small>Sed ut perspiciatis unde</small></p>
  </section>

  <footer class="site-footer">
    <div class="footer-brand"><span class="brand-dot"></span><span class="brand-name">Aurelle Goods</span></div>
    <div class="contact" style="left:96px"><span class="contact-icon"><svg viewBox="0 0 24 24"><path d="M6.6 10.8a15 15 0 0 0 6.6 6.6l2.2-2.2c.3-.3.7-.4 1-.2 1.1.4 2.3.6 3.6.6.6 0 1 .4 1 1V20c0 .6-.4 1-1 1A17 17 0 0 1 3 4c0-.6.4-1 1-1h3.5c.6 0 1 .4 1 1 0 1.3.2 2.5.6 3.6.1.3 0 .7-.2 1z"/></svg></span><span>Phone<br>000.121.1231</span></div>
    <div class="contact" style="left:297px"><span class="contact-icon"><svg viewBox="0 0 24 24"><path d="M2 5h20v14H2zm2 2v.5l8 5 8-5V7l-8 5z"/></svg></span><span>Email<br>info@company.com</span></div>
    <div class="contact" style="left:484px"><span class="contact-icon"><svg viewBox="0 0 24 24"><path d="M12 2a7 7 0 0 1 7 7c0 5-7 13-7 13S5 14 5 9a7 7 0 0 1 7-7zm0 4a3 3 0 1 0 0 6 3 3 0 0 0 0-6z"/></svg></span><span>154 Lorem Ipsum<br>Dummy Lorem</span></div>
    <div class="social"><span></span><span></span><span></span><span></span><span></span></div>
    <p class="copyright">© Copyright 2022 Aurelle Goods.All Rights Reserved.<u>Meet The Team</u></p>
    <p class="page-code">C2</p>
  </footer>

  <div class="mega-menu">
    <div class="menu-col" style="left:13px;top:14px"><h4>BATH</h4><ul><li>Bath Salts</li><li>Soap Base</li><li>Bath Bombs</li><li>Shower Steamers</li></ul></div>
    <div class="menu-col" style="left:122px;top:14px"><h4>BODY</h4><ul><li>Body Butter</li><li>Massage Butter</li></ul></div>
    <div class="menu-col" style="left:122px;top:78px"><h4>KIDS</h4><ul><li>Bath crayons</li></ul></div>
    <div class="menu-col" style="left:229px;top:14px"><h4>FACE</h4><ul><li>Lip balm</li><li>Beard balm</li></ul></div>
    <div class="menu-col" style="left:229px;top:78px"><h4>PETS</h4><ul><li>Paw Mate</li></ul></div>
    <div class="menu-col" style="left:321px;top:14px"><h4>CANDLES</h4><ul><li>Soap</li><li>Bees wax</li><li>Soap coconut</li><li>Wax taste</li></ul></div>
  </div>
</section>

</body>
</html>
```